Marnick Building Materials letterhead template

Simple but professional letterhead template for business communication.
LOGO/name in upper left, balanced by company contact info on right upper.
Subject description, date...
addressee, cc: and BC: if applicable editable info..

Need extra days to review

```html
<!DOCTYPE html>
<html lang="en">
<head>
<meta charset="utf-8">
<title>Marnick Building Materials – Letterhead</title>
<link href="https://fonts.googleapis.com/css2?family=Noto+Sans:wght@400;700&display=swap" rel="stylesheet">
<style>
  :root {
    --brand-blue: #2a5caa;
    --brand-blue-soft: #d6e0f0;
    --ink: #231f20;
    --paper: #ffffff;
  }
  * { margin: 0; padding: 0; box-sizing: border-box; }
  html, body { width: 849px; height: 1200px; overflow: hidden; background: var(--paper); }
  .letterhead {
    position: relative;
    width: 849px;
    height: 1200px;
    overflow: hidden;
    background: var(--paper);
    font-family: "Noto Sans", Arial, sans-serif;
    color: var(--ink);
  }
  .brand-name {
    position: absolute;
    left: 57px;
    top: 70px;
    color: var(--brand-blue);
    font-weight: 700;
    font-size: 22px;
    line-height: 28px;
  }
  .contact {
    position: absolute;
    left: 618px;
    top: 46px;
    list-style: none;
    color: var(--brand-blue);
    font-size: 13.5px;
    line-height: 20px;
  }
  .meta {
    position: absolute;
    left: 57px;
    color: var(--brand-blue);
    font-size: 15.5px;
    line-height: 20.5px;
  }
  .meta-date { top: 176px; }
  .meta-recipients { top: 217px; }
  .meta-subject { top: 299px; font-weight: 700; }
  .letter-body {
    position: absolute;
    left: 56px;
    width: 723px;
    font-size: 15.6px;
    line-height: 19.9px;
  }
  .salutation { top: 386px; font-weight: 700; }
  .line {
    display: block;
    white-space: nowrap;
    text-align: justify;
    text-align-last: justify;
  }
  .line-end { text-align-last: left; }
  .p1 { top: 426px; }
  .p2 { top: 586px; }
  .p3 { top: 725px; }
  .p4 { top: 825px; }
  .closing { top: 905px; }
  .signature {
    position: absolute;
    left: 57px;
    top: 940px;
    width: 280px;
    height: 90px;
    background: linear-gradient(90deg, #eeeeee, #f7f7f7);
    border-radius: 6px;
  }
  .corner-shapes {
    position: absolute;
    left: 0;
    top: 0;
  }
</style>
</head>
<body>
<main class="letterhead">
  <header>
    <p class="brand-name">Marnick Building Materials</p>
    <ul class="contact">
      <li>Address</li>
      <li>Telephone</li>
      <li>Email</li>
      <li>Website</li>
    </ul>
  </header>

  <p class="meta meta-date">Date:</p>
  <p class="meta meta-recipients">Addressee:<br>CC:<br>BC:</p>
  <p class="meta meta-subject">Subject:</p>

  <p class="letter-body salutation">Dear Sir / Madam</p>

  <p class="letter-body p1">
    <span class="line">Lorem ipsum dolor sit amet, consectetuer adipiscing elit, sed diam nonummy nibh euismod</span>
    <span class="line">tincidunt ut laoreet dolore magna aliquam erat volutpat. Ut wisi enim ad minim veniam, quis</span>
    <span class="line">nostrud exerci tation ullamcorper suscipit lobortis nisl ut aliquip ex ea commodo consequat.</span>
    <span class="line">Duis autem vel eum iriure dolor in hendrerit in vulputate velit esse molestie consequat, vel illum</span>
    <span class="line">dolore eu feugiat nulla facilisis at vero eros et accumsan et iusto odio dignissim qui blandit</span>
    <span class="line line-end">praesent luptatum zzril delenit augue duis dolore te feugait nulla facilisi.</span>
    <span class="line line-end">suscipit lobortis nisl ut aliquip ex ea commodo consequat.</span>
  </p>

  <p class="letter-body p2">
    <span class="line">Lorem ipsum dolor sit amet, consectetuer adipiscing elit, sed diam nonummy nibh euismod</span>
    <span class="line">nostrud exerci tation ullamcorper suscipit lobortis nisl ut aliquip ex ea commodo consequat.</span>
    <span class="line">Duis autem vel eum iriure dolor in hendrerit in vulputate velit esse molestie consequat, vel</span>
    <span class="line line-end">blandit praesent luptatum zzril delenit augue duis dolore te feugait nulla facilisi.</span>
    <span class="line">dolore magna aliquam erat volutpat. Ut wisi enim ad minim veniam, quis nostrud exerci tation</span>
    <span class="line line-end">ullamcorper suscipit lobortis nisl ut aliquip ex ea commodo consequat.</span>
  </p>

  <p class="letter-body p3">
    <span class="line">Lorem ipsum dolor sit amet, consectetuer adipiscing elit, sed diam nonummy nibh euismod</span>
    <span class="line">tincidunt ut laoreet dolore magna aliquam erat volutpat. Ut wisi enim ad minim veniam, quis</span>
    <span class="line">nostrud exerci tation ullamcorper iusto odio dignissim qui blandit praesent luptatum zzril</span>
    <span class="line line-end">delenit augue duis dolore te feugait nulla facilisi.</span>
  </p>

  <p class="letter-body p4">
    <span class="line">Lorem ipsum dolor sit amet, cons ectetuer adipiscing elit, sed diam nonummy nibh euismod</span>
    <span class="line">tincidunt ut laoreet dolore magna aliquam erat volutpat. Ut wisi enim ad minim veniam, quis</span>
    <span class="line line-end">nostrud exerci tation ullamcorper suscipit lobortis nisl ut aliquip ex ea commodo consequat.</span>
  </p>

  <p class="letter-body closing">Yours Sinciery,</p>

  <div class="signature" role="img" aria-label="Handwritten signature"></div>

  <svg class="corner-shapes" width="849" height="1200" viewBox="0 0 849 1200" aria-hidden="true">
    <path d="M536 1200 A 60 60 0 0 1 596 1151 L 849 1151 L 849 1200 Z" fill="var(--brand-blue-soft)"/>
    <path d="M647 1200 A 70 70 0 0 1 710 1140 L 849 1140 L 849 1200 Z" fill="var(--brand-blue)"/>
  </svg>
</main>
</body>
</html>
```